Checkout sign

Wall sign for clinic checkout.
“The Good Lord does ALL the healing..
But we DO collect the co-pay”

Add Celtic cross at top and our logo on bottom

```html
<!DOCTYPE html>
<html lang="en">
<head>
<meta charset="utf-8">
<title>Checkout Sign – Harlow Orthopedic Clinic</title>
<link rel="stylesheet" href="https://fonts.googleapis.com/css2?family=Bebas+Neue&family=Cinzel:wght@500&display=swap">
<style>
  :root {
    --backdrop: #9a9a9a;
    --night-top: #2b3a78;
    --night-mid: #1a2350;
    --night-deep: #0a0e22;
    --dusk-pink: #6e3a63;
    --stone: #1d2b55;
    --stone-edge: #4a6a9a;
    --paper: #ffffff;
    --brand-blue: #2a1aa8;
    --brand-violet: #3b2bb8;
    --quote-mark: #9a9aa4;
    --quote-text: #ffffff;
  }
  * { box-sizing: border-box; margin: 0; padding: 0; }
  html, body {
    width: 1200px; height: 829px; overflow: hidden;
    background: var(--backdrop);
  }
  .canvas { position: relative; width: 1200px; height: 829px; }
  .sign {
    position: absolute; left: 402px; top: 20px;
    width: 396px; height: 790px;
    background: var(--paper);
    overflow: hidden;
  }
  .sign__sky {
    position: absolute; left: 0; top: 0; width: 396px; height: 560px;
    background:
      radial-gradient(ellipse 60% 30% at 40% 14%, rgba(110,58,99,0.55), transparent 70%),
      radial-gradient(ellipse 70% 40% at 55% 30%, rgba(70,100,180,0.45), transparent 70%),
      linear-gradient(180deg, var(--night-top) 0%, var(--night-mid) 45%, var(--night-deep) 100%);
  }
  .sign__cross-photo {
    position: absolute; left: 108px; top: 42px; width: 170px; height: 230px;
    border-radius: 6px;
    background:
      radial-gradient(ellipse 55% 40% at 50% 35%, rgba(74,106,154,0.55), transparent 75%),
      linear-gradient(180deg, var(--stone) 0%, rgba(20,28,60,0.9) 70%, rgba(10,14,34,0) 100%);
  }
  .sign__wave {
    position: absolute; left: 0; top: 0; width: 396px; height: 790px;
  }
  .quote {
    position: absolute; left: 0; top: 204px; width: 396px;
    font-family: "Bebas Neue", "Oswald", sans-serif;
    font-size: 52px; line-height: 49.5px;
    color: var(--quote-text);
    text-align: center;
    letter-spacing: 0.5px;
  }
  .quote__line { display: block; }
  .quote__mark {
    position: absolute;
    font-family: "Bebas Neue", sans-serif;
    font-size: 90px; line-height: 1;
    color: var(--quote-mark);
  }
  .quote__mark--open { left: 44px; top: 188px; }
  .quote__mark--close { left: 302px; top: 402px; }
  .brand {
    position: absolute; left: 0; top: 543px; width: 396px;
    text-align: center;
    color: var(--brand-blue);
    font-family: "Cinzel", serif;
    font-weight: 500;
  }
  .brand__dot {
    display: block; margin: 0 auto;
    width: 112px; height: 112px; border-radius: 50%;
    border: 4px solid var(--brand-blue);
  }
  .brand__name {
    display: block; margin-top: 6px;
    font-size: 38px; line-height: 40px; letter-spacing: 0.5px;
  }
  .brand__tag {
    display: block; margin-top: 0;
    font-size: 13px; letter-spacing: 1px;
  }
  .brand__web {
    display: block; margin-top: 14px;
    font-size: 22px; letter-spacing: 0.3px;
  }
</style>
</head>
<body>
<main class="canvas">
  <section class="sign">
    <div class="sign__sky"></div>
    <div class="sign__cross-photo" role="img" aria-label="Photo of a Celtic stone cross silhouetted against a dusky blue and pink evening sky"></div>

    <svg class="sign__wave" viewBox="0 0 396 790" aria-hidden="true">
      <path d="M0,575 C40,520 120,485 210,492 C290,498 350,520 396,500 L396,790 L0,790 Z" fill="var(--paper)"/>
      <path d="M18,562 C70,505 160,478 240,500 C300,518 350,528 382,500 C350,540 290,540 230,518 C160,495 80,510 18,562 Z" fill="var(--brand-violet)"/>
    </svg>

    <span class="quote__mark quote__mark--open">&#8216;</span>
    <p class="quote">
      <span class="quote__line">The Good Lord</span>
      <span class="quote__line">Does All</span>
      <span class="quote__line">The Healing..</span>
      <span class="quote__line">But We Do Collect</span>
      <span class="quote__line">The Co-Pay</span>
    </p>
    <span class="quote__mark quote__mark--close">&#8217;</span>

    <div class="brand">
      <span class="brand__dot"></span>
      <span class="brand__name">HARLOW</span>
      <span class="brand__tag">ORTHOPEDIC CLINIC</span>
      <span class="brand__web">WWW.HARLOWORTHO.COM</span>
    </div>
  </section>
</main>
</body>
</html>
```